Silver Creek Plumbing Business card & letter head design

We need a new business card and letter head for our plumbing company called silver creek plumbing. attached is the companys logo. We provide domestic and commercial plumbing services in regional western Australia. We are after Something simple yet nice to look at and something that fits within the trade industry.

Target Market(s)

trade/building industry

Contact Information for Business Card

Darl Hensby
Manager
0461 238 574
enquiries@scplumbwork.net.au
ABN: 47 381 905 462
PCL: 5187

Domestic & Commercial Plumbing
Tip Truck & Excavator hire

Colors

Designer to choose colors to be used in the design.

```html
<!DOCTYPE html>
<html lang="en">
<head>
<meta charset="utf-8">
<title>Silver Creek Plumbing – Stationery</title>
<link href="https://fonts.googleapis.com/css2?family=Lato:wght@400;700;900&display=swap" rel="stylesheet">
<style>
  :root {
    --brand-blue: #0e58a8;
    --ink-grey: #4a4a4a;
    --paper: #ffffff;
    --backdrop: #3b393a;
  }
  * { margin: 0; padding: 0; box-sizing: border-box; }
  html, body { width: 1200px; height: 955px; overflow: hidden; }
  body {
    background: var(--backdrop);
    font-family: "Lato", Arial, sans-serif;
    position: relative;
  }

  .wordmark {
    position: absolute;
    text-align: center;
    font-weight: 900;
    color: var(--brand-blue);
    line-height: 1;
    transform: translateX(-50%);
    white-space: nowrap;
  }
  .wordmark .wordmark-main { display: block; }
  .wordmark .wordmark-sub { display: block; letter-spacing: 0.45em; margin-right: -0.45em; }
  .wordmark--light { color: var(--paper); }

  /* Letterhead */
  .letterhead {
    position: absolute; left: 220px; top: 136px; width: 529px; height: 686px;
    background: var(--paper);
  }
  .letterhead .wordmark { left: 265px; top: 42px; }
  .letterhead .wordmark-main { font-size: 22px; }
  .letterhead .wordmark-sub { font-size: 9px; margin-top: 5px; }
  .letterhead-footer {
    position: absolute; left: 0; bottom: 0; width: 100%; height: 61px;
    background: var(--brand-blue); color: var(--paper);
  }
  .letterhead-contacts { position: absolute; left: 58px; top: 6px; list-style: none; font-size: 8.5px; }
  .letterhead-contacts li { display: flex; align-items: center; height: 10.5px; }
  .letterhead-contacts svg { width: 8px; height: 8px; margin-right: 6px; }
  .letterhead-legal { position: absolute; right: 40px; top: 4px; text-align: right; font-size: 8px; }
  .letterhead-legal .abn { padding-bottom: 4px; border-bottom: 0.6px solid var(--paper); margin-bottom: 4px; }
  .letterhead-legal .services { font-size: 7.5px; line-height: 1.3; }

  /* Business card front */
  .card {
    position: absolute; left: 785px; width: 303px; height: 176px;
    border-radius: 10px; overflow: hidden;
  }
  .card-front { top: 139px; background: var(--paper); }
  .card-front .wordmark { left: 152px; top: 18px; }
  .card-front .wordmark-main { font-size: 17px; }
  .card-front .wordmark-sub { font-size: 7px; margin-top: 4px; }
  .holder-marker { position: absolute; left: 0; top: 88px; width: 10px; height: 21px; background: var(--brand-blue); }
  .holder-name { position: absolute; left: 18px; top: 86px; font-size: 11px; color: var(--brand-blue); }
  .holder-role { position: absolute; left: 18px; top: 100px; font-size: 8.5px; color: var(--ink-grey); }
  .card-contacts { position: absolute; right: 15px; top: 105px; list-style: none; text-align: right; font-size: 8.5px; color: var(--ink-grey); }
  .card-contacts li { display: flex; justify-content: flex-end; align-items: center; height: 11px; }
  .card-contacts svg { width: 9px; height: 9px; margin-left: 6px; }
  .card-band {
    position: absolute; left: 0; bottom: 0; width: 100%; height: 26px;
    background: var(--brand-blue); color: var(--paper);
    font-size: 8px; font-weight: 700; text-align: center; line-height: 22px;
  }

  /* Business card back */
  .card-back { top: 325px; background: var(--brand-blue); }
  .card-back .wordmark { left: 210px; top: 20px; }
  .card-back .wordmark-main { font-size: 18px; }
  .card-back .wordmark-sub { font-size: 7.5px; margin-top: 4px; }
  .service-tab {
    position: absolute; left: 0; top: 135px; width: 200px; height: 33px;
    background: var(--paper);
    clip-path: polygon(0 0, 182px 0, 200px 100%, 0 100%);
    color: var(--brand-blue); font-size: 9.5px; line-height: 12px;
    padding: 5px 0 0 0;
  }
  .service-tab p { width: 188px; text-align: center; }
</style>
</head>
<body>

<section class="letterhead" aria-label="Letterhead">
  <div class="wordmark">
    <span class="wordmark-main">SILVER CREEK</span>
    <span class="wordmark-sub">PLUMBING</span>
  </div>
  <footer class="letterhead-footer">
    <ul class="letterhead-contacts">
      <li><svg viewBox="0 0 10 10"><circle cx="5" cy="5" r="4.4" fill="none" stroke="#fff" stroke-width="0.8"/><path d="M3 4h4l-.5 2.5h-3z" fill="#fff"/></svg>0461 238 574</li>
      <li><svg viewBox="0 0 10 10"><circle cx="5" cy="5" r="4.4" fill="none" stroke="#fff" stroke-width="0.8"/><rect x="2.8" y="3.5" width="4.4" height="3" fill="#fff"/></svg>enquiries@scplumbwork.net.au</li>
      <li><svg viewBox="0 0 10 10"><circle cx="5" cy="5" r="4.4" fill="none" stroke="#fff" stroke-width="0.8"/><circle cx="5" cy="5" r="2.5" fill="none" stroke="#fff" stroke-width="0.6"/><path d="M2.5 5h5M5 2.5v5" stroke="#fff" stroke-width="0.5"/></svg>www.scplumbwork.net.au</li>
    </ul>
    <div class="letterhead-legal">
      <p class="abn">ABN: 47 381 905 462, PCL: 5187</p>
      <p class="services">Domestic &amp; Commercial Plumbing<br>Tip Truck &amp; Excavator hire</p>
    </div>
  </footer>
</section>

<section class="card card-front" aria-label="Business card front">
  <div class="wordmark">
    <span class="wordmark-main">SILVER CREEK</span>
    <span class="wordmark-sub">PLUMBING</span>
  </div>
  <span class="holder-marker"></span>
  <p class="holder-name">Darl Hensby</p>
  <p class="holder-role">Manager</p>
  <ul class="card-contacts">
    <li>0461 238 574<svg viewBox="0 0 10 10"><path d="M1 3.5q4-3 8 0v1.5h-2v-1h-4v1h-2z M2.5 5h5l1 3h-7z" fill="#0e58a8"/></svg></li>
    <li>enquiries@scplumbwork.net.au<svg viewBox="0 0 10 10"><rect x="1" y="2.5" width="8" height="6" fill="none" stroke="#0e58a8" stroke-width="0.9"/><path d="M1 2.5l4 3.2 4-3.2" fill="none" stroke="#0e58a8" stroke-width="0.9"/></svg></li>
    <li>scplumbwork.net.au<svg viewBox="0 0 10 10"><circle cx="5" cy="5" r="4" fill="none" stroke="#0e58a8" stroke-width="0.9"/><ellipse cx="5" cy="5" rx="1.8" ry="4" fill="none" stroke="#0e58a8" stroke-width="0.7"/><path d="M1 5h8" stroke="#0e58a8" stroke-width="0.7"/></svg></li>
  </ul>
  <div class="card-band">ABN: 47 381 905 462, PCL: 5187</div>
</section>

<section class="card card-back" aria-label="Business card back">
  <div class="wordmark wordmark--light">
    <span class="wordmark-main">SILVER CREEK</span>
    <span class="wordmark-sub">PLUMBING</span>
  </div>
  <div class="service-tab">
    <p>Domestic &amp; Commercial Plumbing</p>
    <p>Tip Truck &amp; Excavator hire</p>
  </div>
</section>

</body>
</html>
```